Business Card Design Project

We are a commercial talent casting company, a very "now" company. We need a new business card that is both current, graphic and elegantly interesting. As we are a service business,
we need something that will attract the attention of new clients,
yet project a business that is 25 years old.

Industry/Entity Type

Business

Requirements
Must have
• 1. Logo - Nora Quillan Casting
2. Address - 47 Thornbury Street
New York, New York 10010
3. Phone - 212-738-4192
4. E-Mail - Casting@noraquillan.example

Nice to have
• Would like the card in black and white with the only accent
color being red.

```html
<!DOCTYPE html>
<html lang="en">
<head>
<meta charset="utf-8">
<title>Nora Quillan Casting — Business Card</title>
<link rel="stylesheet" href="https://fonts.googleapis.com/css2?family=Didact+Gothic&display=swap">
<style>
  :root {
    --card-black: #0b0a0a;
    --ink-white: #f2f2f2;
    --accent-red: #e0242b;
    --page-white: #ffffff;
    --label-ink: #1a1a1a;
  }
  * { margin: 0; padding: 0; box-sizing: border-box; }
  html, body {
    width: 1200px;
    height: 900px;
    overflow: hidden;
    background: var(--page-white);
    font-family: "Didact Gothic", sans-serif;
  }
  .canvas {
    position: relative;
    width: 1200px;
    height: 900px;
  }
  .side-label {
    position: absolute;
    font-size: 58px;
    color: var(--label-ink);
    letter-spacing: 1px;
  }
  .side-label--back { left: 230px; top: 50px; }
  .side-label--front { left: 800px; top: 780px; }

  .card {
    position: absolute;
    width: 700px;
    height: 400px;
    background: var(--card-black);
    border-radius: 90px 14px 90px 14px;
    color: var(--ink-white);
  }
  .card--back { left: 440px; top: 40px; }
  .card--front { left: 60px; top: 460px; }

  .brand {
    position: absolute;
    display: flex;
    align-items: center;
    gap: 12px;
    font-size: 30px;
    color: var(--ink-white);
    white-space: nowrap;
  }
  .brand__square {
    width: 22px;
    height: 22px;
    background: var(--accent-red);
  }
  .card--back .brand { right: 40px; top: 40px; font-size: 28px; }
  .card--front .brand { left: 44px; bottom: 44px; font-size: 36px; }
  .card--front .brand__square { width: 26px; height: 26px; }

  .contact-list {
    position: absolute;
    left: 60px;
    top: 130px;
    list-style: none;
    font-size: 27px;
    line-height: 1.3;
  }
  .contact-list__item {
    display: flex;
    align-items: flex-start;
    gap: 18px;
    margin-bottom: 30px;
  }
  .contact-icon {
    flex: none;
    width: 24px;
    height: 24px;
    margin-top: 4px;
    fill: var(--accent-red);
  }
  .email-at { color: var(--accent-red); }
</style>
</head>
<body>
<main class="canvas">
  <span class="side-label side-label--back">Back</span>
  <span class="side-label side-label--front">Front</span>

  <section class="card card--back" aria-label="Card back">
    <div class="brand">
      <span class="brand__name">Nora Quillan Casting</span>
      <span class="brand__square"></span>
    </div>
    <ul class="contact-list">
      <li class="contact-list__item">
        <svg class="contact-icon" viewBox="0 0 24 24" aria-hidden="true">
          <path d="M12 2 1 12h3v10h6v-6h4v6h6V12h3z"/>
        </svg>
        <span>47 Thornbury Street<br>New York, New York 10010</span>
      </li>
      <li class="contact-list__item">
        <svg class="contact-icon" viewBox="0 0 24 24" aria-hidden="true">
          <path d="M6.6 10.8a15 15 0 0 0 6.6 6.6l2.2-2.2a1 1 0 0 1 1-.25 11.4 11.4 0 0 0 3.6.57 1 1 0 0 1 1 1V20a1 1 0 0 1-1 1A17 17 0 0 1 3 4a1 1 0 0 1 1-1h3.5a1 1 0 0 1 1 1c0 1.25.2 2.45.57 3.57a1 1 0 0 1-.25 1z"/>
        </svg>
        <span>212-738-4192</span>
      </li>
      <li class="contact-list__item">
        <svg class="contact-icon" viewBox="0 0 24 24" aria-hidden="true">
          <path d="M2 6h20v13H2zm2 2v.5l8 5 8-5V8l-8 5z"/>
        </svg>
        <span>Casting<span class="email-at">@</span>noraquillan.example</span>
      </li>
    </ul>
  </section>

  <section class="card card--front" aria-label="Card front">
    <div class="brand">
      <span class="brand__name">Nora Quillan Casting</span>
      <span class="brand__square"></span>
    </div>
  </section>
</main>
</body>
</html>
```